Etiketten-Design für Whisky
Ich bin sehr zufrieden mit der Arbeit von Pelnirot. Auch bei der Nachbearbeitung ist er sehr gut auf meine Wünsche und Vorschläge eingegangen und hat sie zeitnah umgesetzt.
Zielgruppe
Ich habe vor 4 Jahren meine Leidenschaft für Whisk(e)y entdeckt. Vor drei Jahren habe ich bei einer Distellerie mein eigenes Fass (50 Liter) Whisky gebrannt und dann das Fass in meinem Keller eingelagert.
Daurauf hin habe ich meinen Keller in eine private Whisky-Bar umgebaut, damit das Fass in 'würdigem' Rahmen reifen kann. Die Bar habe ich dann nach Südstaaten-Vorbild 'Rusty Bugle Saloon' benannt.
Aufgabenstellung
Es geht um das Feeling eines alten Saloon's in Amerika mit 'Klimpermusik', Poker, Western etc.
Das Design soll eher 'old-school' / retro aber trotzdem zeitgemäss/cool aussehen.
Eine Etikette ähnlich einem 'Western-Steckbrief' mit einem colen Phantombild z.b. von einem Tier als Cowboy wäre auch noch eine Idee.
Ein Design angelehnt an Steampunk wäre vielleicht auch eine Variante.
Wichtig ist auch, dass durch die Etikette nicht zuviel von der Flasche zugeklebt wird, und man die Farbe des Whiskey's noch gut sieht.
Ich habe noch einige Bilder meiner Bar raufgeladen damit man einen Eindruck hat. Materialien sind roher Stahl, Holz, Messing, Kupfer und viel 'schwarz'
Den Flaschentyp habe ich auch festgelegt (Masszeichnung + Bilder habe ich raufgeladen.
Informationen die auf die Flasche sollen sind in einer pdf-Datei zusammengefasst.
Auf der Etikette soll irgendwo noch 'KT4512' (meine Initialen + postleitzahl) integriert sein.

```html
<!DOCTYPE html>
<html lang="en">
<head>
<meta charset="utf-8">
<title>Rusty Bugle Rye Whiskey – Label Set</title>
<link rel="stylesheet" href="https://fonts.googleapis.com/css2?family=Rye&family=Oswald:wght@400;500&family=Pirata+One&display=swap">
<style>
  :root {
    --bg: #e3e3e5;
    --label-black: #0b0b0b;
    --gold: #d9a62e;
    --gold-light: #f3d27a;
    --gold-dark: #9a6b12;
    --white: #ffffff;
    --grey-mark: #8d8d8f;
    --grey-mark-light: #b9b9bb;
  }
  * { box-sizing: border-box; margin: 0; padding: 0; }
  html, body { width: 1172px; height: 1200px; overflow: hidden; }
  body { background: var(--bg); font-family: "Oswald", sans-serif; position: relative; }

  /* Brand lockup */
  .lockup { position: absolute; left: 436px; top: 50px; width: 300px; text-align: center; }
  .lockup__art { width: 240px; height: 130px; margin: 0 auto;
    background: radial-gradient(ellipse at 50% 70%, var(--grey-mark-light), rgba(185,185,187,0) 70%); }
  .lockup__name { font-family: "Rye", serif; color: var(--grey-mark); line-height: 1; margin-top: 4px; }
  .lockup__the { display: block; font-size: 18px; text-align: left; padding-left: 52px; margin-bottom: 2px; }
  .lockup__word { display: block; font-size: 50px; }
  .lockup__sub { font-family: "Pirata One", cursive; color: var(--grey-mark); font-size: 28px; margin-top: 4px; }

  /* Front label */
  .front-label { position: absolute; left: 150px; top: 570px; width: 340px; height: 420px; }
  .front-label__shape { position: absolute; inset: 0; }
  .front-label__content { position: absolute; inset: 0; text-align: center; color: var(--white); }
  .front-label__art { position: absolute; left: 30px; top: 14px; width: 280px; height: 140px;
    background: radial-gradient(ellipse at 50% 95%, var(--gold-light) 0%, var(--gold) 30%, rgba(217,166,46,0) 72%); }
  .front-label__name { position: absolute; left: 0; right: 0; top: 150px; font-family: "Rye", serif; font-weight: 400; color: var(--white); line-height: 1; }
  .front-label__the { display: block; font-size: 18px; text-align: left; padding-left: 70px; margin-bottom: 2px; }
  .front-label__word { display: block; font-size: 54px; line-height: 1.05; }
  .front-label__type { position: absolute; left: 0; right: 0; top: 290px; font-family: "Pirata One", cursive; color: var(--gold); font-size: 30px; line-height: 1.2; }
  .front-label__rule { position: absolute; left: 36px; right: 36px; border-top: 2px dotted var(--gold); }
  .front-label__rule--top { top: 334px; }
  .front-label__rule--bottom { top: 397px; }
  .front-label__facts { position: absolute; left: 0; right: 0; top: 338px; font-size: 12.5px; line-height: 1.65; }
  .front-label__facts .sep { color: var(--white); padding: 0 5px; }
  .front-label__code { position: absolute; left: 50%; top: 388px; transform: translateX(-50%);
    border: 1px solid var(--white); border-radius: 4px; background: var(--label-black);
    font-family: "Courier New", monospace; font-size: 12px; padding: 0 10px; letter-spacing: 1px; }

  /* Neck label */
  .neck-label { position: absolute; left: 256px; top: 306px; width: 124px; height: 60px;
    background: var(--label-black); display: flex; align-items: center; justify-content: center; gap: 8px; }
  .neck-label__mark { width: 10px; height: 10px; border-radius: 50%; background: var(--gold); }
  .neck-label__name { font-family: "Rye", serif; color: var(--gold); font-size: 28px; }

  /* Back label */
  .back-label { position: absolute; left: 770px; top: 772px; width: 168px; height: 170px;
    background: var(--label-black); border-radius: 9px; color: var(--white); text-align: center; padding: 10px 10px; }
  .back-label__name { font-family: "Rye", serif; font-size: 18px; line-height: 1; }
  .back-label__facts { list-style: none; font-size: 7.5px; line-height: 1.4; margin-top: 6px; }
  .back-label__facts li + li { margin-top: 4px; }
  .back-label__bottle { display: flex; margin-top: 8px; border: 1px solid var(--white); border-radius: 3px; overflow: hidden; height: 18px; }
  .back-label__bottle-tag { font-size: 8px; padding: 2px 4px; }
  .back-label__bottle-field { flex: 1; background: var(--white); }
  .back-label__type { font-family: "Pirata One", cursive; font-size: 12px; margin-top: 5px; }
  .back-label__type .arrow { font-family: "Oswald", sans-serif; font-size: 9px; padding: 0 4px; }
</style>
</head>
<body>

  <section class="lockup">
    <div class="lockup__art" role="img" aria-label="Engraved rooster with sheriff star and bag before a radiating sunburst"></div>
    <div class="lockup__name">
      <span class="lockup__the">The</span>
      <span class="lockup__word">Rusty</span>
      <span class="lockup__word">Bugle</span>
    </div>
    <div class="lockup__sub">Rye Whiskey</div>
  </section>

  <section class="neck-label">
    <span class="neck-label__mark"></span>
    <span class="neck-label__name">RB</span>
  </section>

  <section class="front-label">
    <svg class="front-label__shape" viewBox="0 0 340 420" width="340" height="420" aria-hidden="true">
      <path d="M0 64 Q0 50 16 50 L70 50 Q170 -30 270 50 L324 50 Q340 50 340 64 L340 404 Q340 420 324 420 L16 420 Q0 420 0 404 Z" fill="#0b0b0b"/>
    </svg>
    <div class="front-label__content">
      <div class="front-label__art" role="img" aria-label="Engraved rooster with sheriff star and bag before a golden sunburst"></div>
      <h1 class="front-label__name">
        <span class="front-label__the">The</span>
        <span class="front-label__word">Rusty</span>
        <span class="front-label__word">Bugle</span>
      </h1>
      <div class="front-label__type">Rye Whiskey</div>
      <div class="front-label__rule front-label__rule--top"></div>
      <p class="front-label__facts">
        700 ml<span class="sep">|</span>48% Alc.<span class="sep">|</span>Single Quarter-Cask<br>
        Distillation Date: 22.04.2017<span class="sep">|</span>Bottling Date: 23.04.2020
      </p>
      <div class="front-label__rule front-label__rule--bottom"></div>
      <div class="front-label__code">KT4512</div>
    </div>
  </section>

  <section class="back-label">
    <div class="back-label__name">Rusty<br>Bugle</div>
    <ul class="back-label__facts">
      <li>• Pot-distilled from 100% Rye Malt over Woodfire</li>
      <li>• Matured in a Islay-Whisky Oak-Cask<br>&amp; finished in a Redwine Chestnut-Cask</li>
      <li>• Non-Chill-filtered • No Colouring</li>
    </ul>
    <div class="back-label__bottle">
      <span class="back-label__bottle-tag">Bottle No</span>
      <span class="back-label__bottle-field"></span>
    </div>
    <div class="back-label__type"><span class="arrow">»</span>Rye Whiskey<span class="arrow">«</span></div>
  </section>

</body>
</html>
```